Brimble Diecast Torvel Collectables Website

looking for a vibrant web site marketplace built for diecast car enthusiasts to buy, sell, and trade with ease. Whether you're looking to showcase your own collection or discover rare and exciting models, our site makes the process simple and enjoyable. Clients can browse a curated inventory of high‑quality diecast cars, connect with fellow collectors, and find the perfect pieces to expand their collection. With a smooth user experience and a community-driven spirit, we’re the go‑to destination for anyone passionate about diecast cars.

Target Market(s)

diecast collectors

Industry/Entity Type

Diecast Collectables

Coding

Coded - Design and coding required

Number of Pages Required

3 page

Font styles to use
Sans Serif

Colors
EE7325
F08F49
F5BC92
FAE3D3
FDF4ED

Requirements
Must have
• Cool look and feel. Woo commerce page to post and sell my inventory
Nice to have
• page for users to post their cars or looking for trades.
Should not have
• look cheap

```html
<!DOCTYPE html>
<html lang="en">
<head>
<meta charset="utf-8">
<title>Brimble Diecast — The Ultimate Hub for Diecast Collectors</title>
<link href="https://fonts.googleapis.com/css2?family=Montserrat:wght@400;500;600;700;800&family=Oswald:wght@300;400&display=swap" rel="stylesheet">
<style>
:root{
  --orange:#EE7325;
  --orange-2:#F08F49;
  --peach:#F5BC92;
  --cream:#FAE3D3;
  --cream-2:#FDF4ED;
  --ink:#141414;
  --text:#333333;
  --muted:#555555;
  --dark:#232323;
  --line:#EFD8C6;
}
*{margin:0;padding:0;box-sizing:border-box}
html,body{width:1200px;height:4710px;overflow:hidden}
body{position:relative;background:#fff;font-family:'Montserrat',sans-serif;color:var(--text)}
.abs{position:absolute}
.eyebrow{font-family:'Oswald',sans-serif;font-weight:300;font-size:17px;letter-spacing:1.5px;color:var(--orange);text-transform:uppercase}
.heading{font-weight:700;font-size:38px;color:var(--ink);text-transform:uppercase;letter-spacing:.5px;line-height:1}
.heading span{color:var(--orange)}
.rule{width:58px;height:3px;background:var(--orange)}
.btn{display:flex;align-items:center;justify-content:center;gap:6px;font-weight:700;font-size:15px;text-transform:uppercase;letter-spacing:.3px;text-decoration:none}
.btn svg{width:14px;height:14px}
.btn-orange{background:var(--orange);color:#fff}
.btn-white{background:#fff;color:var(--orange)}
.btn-dark{background:var(--ink);color:#fff}

/* hero */
.hero{left:9px;top:9px;width:1182px;height:671px;border-radius:18px;overflow:hidden;
  background:linear-gradient(180deg,#f7dcb8 0%,#f0a868 18%,#e0743a 38%,#c4522a 55%,#b86a4a 68%,#9c9390 80%,#7e7a7c 100%)}
.hero-art{position:absolute;inset:0}
.brand{left:70px;top:70px;display:flex;align-items:center;gap:10px}
.brand-dot{width:20px;height:20px;border-radius:50%;background:var(--orange)}
.brand-name{font-weight:800;font-size:17px;color:var(--ink);letter-spacing:.5px;text-transform:uppercase}
.nav{left:351px;top:64px}
.nav a{position:absolute;font-weight:600;font-size:14px;color:var(--ink);text-decoration:none;white-space:nowrap}
.nav a.active{border-bottom:2px solid var(--orange);padding-bottom:4px}
.cart{left:1064px;top:55px;width:38px;height:38px;border-radius:50%;background:var(--orange);display:flex;align-items:center;justify-content:center}
.hero-title{left:0;width:1200px;top:168px;text-align:center;font-weight:800;font-size:56px;color:var(--ink);line-height:1}
.hero-sub{left:0;width:1200px;top:231px;text-align:center;font-weight:700;font-size:37px;color:var(--ink);line-height:1}
.hero-buy{left:410px;top:297px;width:176px;height:46px}
.hero-sell{left:605px;top:297px;width:168px;height:46px}

/* collections */
.card{top:860px;width:284px;height:340px;border:1px solid var(--line);background:#fffaf6;border-radius:4px;text-align:center}
.card-img{position:absolute;left:30px;top:36px;width:224px;height:118px;border-radius:4px}
.card h3{position:absolute;left:0;right:0;top:200px;font-size:18px;font-weight:600;color:var(--ink)}
.card p{position:absolute;left:22px;right:22px;top:232px;font-size:11px;line-height:15px;color:var(--muted)}
.card .price{position:absolute;left:0;right:0;top:276px;font-size:24px;font-weight:700;color:var(--orange)}
.arrow-btn{top:760px;width:46px;height:46px;border-radius:50%;background:var(--orange);display:flex;align-items:center;justify-content:center}

/* sell / trade */
.split{left:48px;top:1275px;width:1128px;height:527px;border-radius:6px;overflow:hidden;display:flex}
.split-left{width:546px;height:100%;background:linear-gradient(180deg,#fbeadb 0%,#f8e0cd 60%,#f6d6bf 100%)}
.split-right{flex:1;height:100%;background:linear-gradient(180deg,#f28a3e 0%,#ee7325 55%,#e66a1f 100%)}
.split-block{top:1350px;display:flex;flex-direction:column;align-items:center;text-align:center}
.split-block .eyebrow{font-size:15px}
.split-block h2{margin-top:6px;font-size:37px;font-weight:700;letter-spacing:.5px;line-height:1.1}
.split-block p{margin-top:22px;width:450px;font-size:15px;line-height:25px}
.split-block .btn{margin-top:22px;height:46px;width:174px}

/* community */
.photo{border-radius:6px}
.community{left:671px;top:2030px;width:470px}
.community h2{font-size:38px;font-weight:700;color:var(--ink);margin-top:12px}
.community p{font-size:17px;line-height:26px;color:var(--text);margin-top:22px}
.community p + p{margin-top:14px}

/* testimonials */
.testi-band{left:0;top:2520px;width:1200px;height:571px;background:linear-gradient(180deg,#fdf1e6 0%,#fbe7d6 50%,#fdf4ed 100%)}
.tcard{background:#fff;border:1px solid #f2e4d8;border-radius:6px;box-shadow:0 6px 18px rgba(200,140,90,.15);padding:26px 30px 24px;width:316px}
.stars{color:var(--orange);font-size:16px;letter-spacing:4px;line-height:1}
.tcard p{margin-top:12px;font-size:11.5px;line-height:20px;color:#444}
.person{margin-top:16px;display:flex;align-items:center;gap:10px;font-size:13px;font-weight:600;color:var(--ink)}
.avatar{width:34px;height:34px;border-radius:50%;background:#c9b8a8}
.quote{position:absolute;right:26px;bottom:6px;font-size:64px;line-height:1;color:var(--peach);font-family:Georgia,serif}
.dot{top:3014px;width:11px;height:11px;border-radius:50%;background:var(--peach)}

/* blog */
.post{top:3276px;width:322px;height:419px;border:1px solid #e8e2dd;background:#fff}
.post-img{position:absolute;left:0;top:0;width:100%;height:236px}
.post-date{position:absolute;left:2px;top:208px;height:24px;padding:0 10px;background:var(--orange);color:#fff;font-family:'Oswald',sans-serif;font-size:13px;display:flex;align-items:center;gap:6px}
.post h3{position:absolute;left:34px;right:24px;top:270px;font-size:17px;line-height:22px;font-weight:700;color:var(--ink)}
.post p{position:absolute;left:34px;right:24px;top:322px;font-size:12.5px;line-height:21px;color:#555}
.post a{position:absolute;left:34px;top:376px;font-size:12.5px;font-weight:700;color:var(--orange);text-decoration:underline}

/* cta */
.dark-band{left:0;top:4161px;width:1200px;height:549px;background:var(--dark)}
.cta{left:99px;top:3762px;width:1009px;height:492px;border-radius:16px;overflow:hidden;
  background:linear-gradient(180deg,#ee7325 0%,#e8752f 35%,#d9682c 70%,#c45a26 100%)}
.cta-label{left:0;width:1200px;top:3843px;text-align:center;font-family:'Oswald',sans-serif;font-weight:300;font-size:16px;letter-spacing:1.5px;color:#fff}
.cta-title{left:0;width:1200px;top:3876px;text-align:center;font-weight:700;font-size:35px;line-height:44px;color:#fff;text-transform:uppercase}
.cta-text{left:0;width:1200px;top:3966px;text-align:center;font-size:15px;line-height:26px;color:#fff}
.pill{height:42px;border-radius:22px}

/* footer */
.foot-head{top:4350px;font-weight:700;font-size:18px;color:#fff;text-transform:uppercase}
.foot-list{top:4390px;list-style:none}
.foot-list li{font-size:14px;color:#e8e8e8;height:29px}
.contact-row{display:flex;align-items:center;gap:12px;font-size:14px;color:#fff}
.contact-icon{width:28px;height:28px;border-radius:50%;background:var(--orange);display:flex;align-items:center;justify-content:center}
.social{width:22px;height:22px;border-radius:50%;background:#fff}
</style>
</head>
<body>

<!-- HERO -->
<header class="abs hero">
  <div class="hero-art" role="img" aria-label="Illustrated desert canyon at sunset with a road and a row of sports cars racing toward the viewer"></div>
</header>
<div class="abs brand"><span class="brand-dot"></span><span class="brand-name">Brimble Diecast</span></div>
<nav class="abs nav">
  <a class="active" style="left:0;top:0">HOME</a>
  <a style="left:101px;top:0">SHOP</a>
  <a style="left:198px;top:0">BUY</a>
  <a style="left:284px;top:0">SELL</a>
  <a style="left:373px;top:0">BLOGS</a>
  <a style="left:479px;top:0">ABOUT</a>
  <a style="left:585px;top:0">CONTACT</a>
</nav>
<div class="abs cart" aria-label="Cart">
  <svg width="18" height="18" viewBox="0 0 24 24" fill="#fff"><path d="M3 4h3l2.4 10.2a1 1 0 0 0 1 .8h8.7a1 1 0 0 0 1-.8L21 7H7.2" stroke="#fff" stroke-width="2" fill="none" stroke-linejoin="round"/><circle cx="10" cy="19" r="1.7"/><circle cx="17" cy="19" r="1.7"/></svg>
</div>
<h1 class="abs hero-title">THE ULTIMATE HUB</h1>
<p class="abs hero-sub">FOR DIECAST COLLECTORS</p>
<a class="abs btn btn-orange hero-buy">BUY CARS <svg viewBox="0 0 16 16"><path d="M2 8h11M9 4l4 4-4 4" stroke="currentColor" stroke-width="2" fill="none"/></svg></a>
<a class="abs btn btn-white hero-sell">SELL CARS <svg viewBox="0 0 16 16"><path d="M2 8h11M9 4l4 4-4 4" stroke="currentColor" stroke-width="2" fill="none"/></svg></a>

<!-- BUY DIECAST CARS -->
<p class="abs eyebrow" style="left:91px;top:744px">OUR COLLECTIONS</p>
<h2 class="abs heading" style="left:91px;top:776px">BUY DIECAST <span>CARS</span></h2>
<div class="abs rule" style="left:91px;top:826px"></div>
<div class="abs arrow-btn" style="left:1010px"><svg width="18" height="18" viewBox="0 0 16 16"><path d="M14 8H3M7 4L3 8l4 4" stroke="#fff" stroke-width="2" fill="none"/></svg></div>
<div class="abs arrow-btn" style="left:1069px"><svg width="18" height="18" viewBox="0 0 16 16"><path d="M2 8h11M9 4l4 4-4 4" stroke="#fff" stroke-width="2" fill="none"/></svg></div>

<div class="abs card" style="left:84px">
  <div class="card-img" role="img" aria-label="Silver diecast time-travel coupe model" style="background:linear-gradient(180deg,#eeeeee,#c4c4c4)"></div>
  <h3>CAR HEADING</h3><p>Lorem ipsum dolor sit amet consectetur adipiscing elit sed do eiusmod</p><div class="price">$25.99</div>
</div>
<div class="abs card" style="left:390px">
  <div class="card-img" role="img" aria-label="Black diecast hero car model with yellow accents" style="background:linear-gradient(180deg,#eeeeee,#5a5a50)"></div>
  <h3>CAR HEADING</h3><p>Lorem ipsum dolor sit amet consectetur adipiscing elit sed do eiusmod</p><div class="price">$25.99</div>
</div>
<div class="abs card" style="left:700px">
  <div class="card-img" role="img" aria-label="Red diecast sports coupe model" style="background:linear-gradient(180deg,#f6e2e0,#d84a3a)"></div>
  <h3>CAR HEADING</h3><p>Lorem ipsum dolor sit amet consectetur adipiscing elit sed do eiusmod</p><div class="price">$25.99</div>
</div>
<div class="abs card" style="left:1006px">
  <div class="card-img" role="img" aria-label="Black diecast muscle car model with flame stripes" style="background:linear-gradient(180deg,#eeeeee,#4a4a4a)"></div>
  <h3>CAR HEADING</h3><p>Lorem ipsum dolor sit amet consectetur adipiscing elit sed do eiusmod</p><div class="price">$25.99</div>
</div>

<!-- SELL / TRADE -->
<section class="abs split" role="img" aria-label="Desert canyon backdrop with a flame-painted muscle car, a cactus and a blue tuned sports car along the bottom">
  <div class="split-left"></div>
  <div class="split-right"></div>
</section>
<div class="abs split-block" style="left:48px;width:546px">
  <p class="eyebrow">SELL YOUR CARS</p>
  <h2 style="color:var(--ink)">SELL DIECAST <span style="color:var(--orange)">CARS</span></h2>
  <p style="color:var(--text)">Turn your collection into cash. List your diecast cars in minutes with our simple selling tools and reach thousands of collectors instantly.</p>
  <a class="btn btn-orange">SELL CARS <svg viewBox="0 0 16 16"><path d="M2 8h11M9 4l4 4-4 4" stroke="currentColor" stroke-width="2" fill="none"/></svg></a>
</div>
<div class="abs split-block" style="left:594px;width:582px">
  <p class="eyebrow" style="color:#fff">TRADING NOW</p>
  <h2 style="color:#fff">CARTRADING</h2>
  <p style="color:#fff">Browse verified listings from collectors worldwide. Each listing includes detailed descriptions and photos so you can shop with confidence</p>
  <a class="btn btn-dark">TRADING <svg viewBox="0 0 16 16"><path d="M2 8h11M9 4l4 4-4 4" stroke="currentColor" stroke-width="2" fill="none"/></svg></a>
</div>

<!-- COMMUNITY TRADING -->
<div class="abs photo" role="img" aria-label="Hand holding a small orange diecast sports car" style="left:102px;top:2001px;width:245px;height:410px;background:linear-gradient(180deg,#9aa6ae,#c77a4e 55%,#5a4a44)"></div>
<div class="abs photo" role="img" aria-label="Rows of colourful diecast cars from above" style="left:357px;top:2001px;width:245px;height:199px;background:linear-gradient(135deg,#d8d8d8,#4aa6a0 40%,#e04a3a 70%,#e8c24a)"></div>
<div class="abs photo" role="img" aria-label="Close view of pink and yellow diecast cars" style="left:357px;top:2211px;width:245px;height:200px;background:linear-gradient(135deg,#3a2a2a,#d86a7a 50%,#e8c84a)"></div>
<div class="abs community">
  <p class="eyebrow">JOIN THE COMMUNITY</p>
  <h2>TRADING</h2>
  <p>Prefer to swap? Connect with other collectors and trade models securely through our built in messaging and trade offer system.</p>
  <p>Lorem ipsum dolor sit amet, consectetur adipiscing elit, sed do eiusmod tempor incididunt ut</p>
</div>
<a class="abs btn btn-orange" style="left:671px;top:2328px;width:178px;height:48px">BUY CARS <svg viewBox="0 0 16 16"><path d="M2 8h11M9 4l4 4-4 4" stroke="currentColor" stroke-width="2" fill="none"/></svg></a>

<!-- TESTIMONIALS -->
<section class="abs testi-band"></section>
<p class="abs eyebrow" style="left:0;width:1200px;text-align:center;top:2568px">TESTIMONIALS</p>
<h2 class="abs heading" style="left:0;width:1200px;text-align:center;top:2601px">WHAT PEOPLE <span>SAYS</span></h2>

<div class="abs tcard" style="left:110px;top:2700px">
  <div class="stars">★★★★★</div>
  <p>"Lorem ipsum dolor sit amet, consectetur adipiscing elit, sed do eiusmod tempor incididunt ut labore et dolore magna aliqua Quis ipsum suspendisse ultrices gravida. Risus commodo viverra maecenas accumsan lacus vel"</p>
  <div class="person"><span class="avatar"></span>Joseph Harlow</div><span class="quote">”</span>
</div>
<div class="abs tcard" style="left:452px;top:2692px">
  <div class="stars">★★★★★</div>
  <p>"Lorem ipsum dolor sit amet, consectetur adipiscing elit, sed do eiusmod tempor incididunt ut labore et dolore magna aliqua Qtempor incididunt ut labore et dolore magna aliqua Quis ipsum suspendisse ultrices gravida Risus commodo viverra maecena"</p>
  <div class="person"><span class="avatar"></span>Peter Ashdown</div><span class="quote">”</span>
</div>
<div class="abs tcard" style="left:794px;top:2703px">
  <div class="stars">★★★★★</div>
  <p>"Lorem ipsum dolor sit amet, consectetur adipiscing elit, sed do eiusmod tempor incididunt ut labore et dolore magna aliqua Quis ipsum suspendisse ultrices gravida. Risus commodo viverra maecenas accumsan lacus vel"</p>
  <div class="person"><span class="avatar"></span>Susan Marlowe</div><span class="quote">”</span>
</div>
<span class="abs dot" style="left:556px;background:var(--orange)"></span>
<span class="abs dot" style="left:580px"></span>
<span class="abs dot" style="left:604px"></span>
<span class="abs dot" style="left:628px"></span>

<!-- BLOGS -->
<p class="abs eyebrow" style="left:117px;top:3144px">RECENT POSTS</p>
<h2 class="abs heading" style="left:117px;top:3176px">BLOGS &amp; <span>ARTICLES</span></h2>
<div class="abs rule" style="left:117px;top:3228px"></div>

<article class="abs post" style="left:113px">
  <div class="post-img" role="img" aria-label="Close-up of red vintage diecast race cars" style="background:linear-gradient(135deg,#c8c8c8,#d83a2a 45%,#8a1a14)"></div>
  <span class="post-date">▣ 20 MAR 2026</span>
  <h3>Lorem ipsum dolor sit amet, consectetur adipiscing</h3>
  <p>Quis ipsum suspendisse ultrices gravida ipsum suspendisse ultrices gravida</p>
  <a>LEARN MORE →</a>
</article>
<article class="abs post" style="left:452px">
  <div class="post-img" role="img" aria-label="Retro diecast sports car under neon light" style="background:linear-gradient(135deg,#e85aa8,#4aa0c8 55%,#2a2a3a)"></div>
  <span class="post-date">▣ 20 MAR 2026</span>
  <h3>Lorem ipsum dolor sit amet, consectetur adipiscing</h3>
  <p>Quis ipsum suspendisse ultrices gravida ipsum suspendisse ultrices gravida</p>
  <a>LEARN MORE →</a>
</article>
<article class="abs post" style="left:790px">
  <div class="post-img" role="img" aria-label="Large crowd of colourful diecast cars" style="background:linear-gradient(135deg,#3a6ac8,#e84a3a 35%,#e8c84a 65%,#3aa86a)"></div>
  <span class="post-date">▣ 20 MAR 2026</span>
  <h3>Lorem ipsum dolor sit amet, consectetur adipiscing</h3>
  <p>Quis ipsum suspendisse ultrices gravida ipsum suspendisse ultrices gravida</p>
  <a>LEARN MORE →</a>
</article>

<!-- CTA -->
<section class="abs dark-band"></section>
<section class="abs cta" role="img" aria-label="Illustrated desert canyon with a red and a blue stock car racing in the dust"></section>
<p class="abs cta-label">BUY. SELL. TRADE. COLLECT</p>
<h2 class="abs cta-title">YOUR MARKETPLACE FOR<br>MINIATURE MASTERPIECES</h2>
<p class="abs cta-text">Lorem ipsum dolor sit amet, consectetur adipiscing elit, sed do eiusmod<br>tempor incididunt ut labore et dolore magna aliqua.</p>
<a class="abs btn btn-dark pill" style="left:410px;top:4048px;width:181px">BUY CARS <svg viewBox="0 0 16 16"><path d="M4 12l8-8M6 4h6v6" stroke="currentColor" stroke-width="2" fill="none"/></svg></a>
<a class="abs btn btn-white pill" style="left:605px;top:4048px;width:181px">SELL CARS <svg viewBox="0 0 16 16"><path d="M4 12l8-8M6 4h6v6" stroke="currentColor" stroke-width="2" fill="none"/></svg></a>

<!-- FOOTER -->
<div class="abs" style="left:170px;top:4390px;display:flex;align-items:center;gap:8px">
  <span class="brand-dot"></span><span class="brand-name" style="color:#fff">Brimble Diecast</span>
</div>
<div class="abs social" style="left:179px;top:4494px" aria-label="Social link"></div>
<div class="abs social" style="left:227px;top:4494px" aria-label="Social link"></div>
<div class="abs social" style="left:274px;top:4494px" aria-label="Social link"></div>

<h4 class="abs foot-head" style="left:435px">NAVIGATION</h4>
<ul class="abs foot-list" style="left:435px"><li>Buy</li><li>About</li><li>Sell</li><li>Blog</li></ul>
<h4 class="abs foot-head" style="left:677px">RESOURCES</h4>
<ul class="abs foot-list" style="left:677px"><li>FAQ</li><li>Terms of Use</li><li>Privacy Policy</li><li>Contact</li></ul>
<h4 class="abs foot-head" style="left:898px">CONTACT US</h4>
<div class="abs contact-row" style="left:898px;top:4390px"><span class="contact-icon"><svg width="14" height="14" viewBox="0 0 24 24"><path d="M6.6 10.8a15 15 0 0 0 6.6 6.6l2.2-2.2a1 1 0 0 1 1-.25 11.4 11.4 0 0 0 3.6.57 1 1 0 0 1 1 1V20a1 1 0 0 1-1 1A17 17 0 0 1 3 4a1 1 0 0 1 1-1h3.5a1 1 0 0 1 1 1c0 1.25.2 2.45.57 3.57a1 1 0 0 1-.25 1z" fill="#fff"/></svg></span>(555) 013-2290</div>
<div class="abs contact-row" style="left:898px;top:4434px"><span class="contact-icon"><svg width="14" height="14" viewBox="0 0 24 24"><rect x="3" y="5" width="18" height="14" rx="2" fill="none" stroke="#fff" stroke-width="2"/><path d="M3 7l9 6 9-6" fill="none" stroke="#fff" stroke-width="2"/></svg></span>hello@brimblediecast.example</div>

<div class="abs" style="left:48px;top:4618px;width:1104px;height:1px;background:#444"></div>
<p class="abs" style="left:0;width:1200px;top:4638px;text-align:center;font-size:13px;color:#ddd">Copyright © 2026 Brimble Diecast.com. All Right Reserved</p>

</body>
</html>
```